BRAVEN VOLTWORKS SERVICES needs a vibrant design for electrical contracting work.

I require a card design for my own electrical contracting business. I will be doing a lot of domestic and commercial work, including things such as repairs, maintenance, lighting, installations and various others. LED lighting and energy efficiency will be a big part of my business. I wish not to have childish pictures such as light bulbs in the design, but rather a smart and modern looking card which incorporates my logo colours and perhaps the same lighting strike within the faded background of the card.

Target Market(s)

Residential and Commercial property owners.

Industry/Entity Type

Electrical

Contact Information for Business Card

Dario Pesek
EC40362
Phone Number: 0417 538 924
Email: dario@bravenvoltworks.com

Font styles to use
Serif
Sans Serif

Requirements
Must have
• My Logo and associated colours.
Nice to have
• Some form of shapes splitting the card into different colours related to the colours of my logo. Electric Blue, Silver/Grey and White.
Should not have
• Childish pictures and symbols such as light bulbs.

```html
<!DOCTYPE html>
<html lang="en">
<head>
<meta charset="utf-8">
<title>Braven Voltworks Services – Business Card</title>
<link rel="stylesheet" href="https://fonts.googleapis.com/css2?family=Noto+Serif:wght@400;700&display=swap">
<style>
  :root {
    --electric-blue: #3a51a5;
    --deep-blue: #33479a;
    --silver-grey: #75777b;
    --white: #ffffff;
    --soft-white: #e9ebf4;
    --serif: "Noto Serif", Georgia, serif;
  }
  html, body {
    margin: 0;
    padding: 0;
    overflow: hidden;
    background: var(--white);
  }
  .card {
    position: relative;
    width: 1200px;
    height: 702px;
    overflow: hidden;
    background: var(--electric-blue);
    font-family: var(--serif);
  }
  .card-bands {
    position: absolute;
    inset: 0;
    width: 1200px;
    height: 702px;
  }
  .band-grey { fill: var(--silver-grey); }
  .band-blue { fill: var(--electric-blue); }
  .band-white { fill: var(--white); }
  .faint-disc { fill: var(--deep-blue); opacity: 0.55; }

  .brand {
    position: absolute;
    left: 420px;
    top: 262px;
    transform: translate(-50%, -50%) rotate(-30deg);
    display: flex;
    align-items: center;
    gap: 22px;
    white-space: nowrap;
  }
  .brand-dot {
    width: 96px;
    height: 96px;
    border-radius: 50%;
    background: var(--electric-blue);
    flex: none;
  }
  .brand-name {
    margin: 0;
    font-family: var(--serif);
    font-weight: 700;
    font-size: 50px;
    line-height: 1.08;
    letter-spacing: 2px;
    color: var(--electric-blue);
  }
  .brand-name span { display: block; }

  .contact {
    position: absolute;
    right: 80px;
    top: 515px;
    margin: 0;
    text-align: right;
    color: var(--white);
    font-size: 33px;
    line-height: 42px;
    text-shadow: 1px 2px 3px rgba(0, 0, 0, 0.35);
  }
  .contact-line {
    display: flex;
    justify-content: flex-end;
    align-items: center;
    gap: 10px;
  }
  .contact-value { color: var(--soft-white); }
  .contact-icon {
    width: 30px;
    height: 30px;
    fill: var(--white);
    filter: drop-shadow(1px 2px 2px rgba(0, 0, 0, 0.35));
  }
  .contact-icon.mail { width: 46px; height: 30px; }
</style>
</head>
<body>
<main class="card">
  <svg class="card-bands" viewBox="0 0 1200 702" aria-hidden="true">
    <circle class="faint-disc" cx="905" cy="435" r="225"/>
    <polygon class="band-grey" points="1122,0 1172,0 0,675 0,647"/>
    <polygon class="band-white" points="553,0 1122,0 0,647 0,320"/>
    <polygon class="band-blue" points="514,0 553,0 0,320 0,296"/>
    <polygon class="band-grey" points="0,0 514,0 0,296"/>
  </svg>

  <div class="brand">
    <div class="brand-dot"></div>
    <h1 class="brand-name"><span>BRAVEN VOLTWORKS</span><span>SERVICES</span></h1>
  </div>

  <address class="contact">
    <div class="contact-line">Dario Pesek EC40362</div>
    <div class="contact-line">
      <svg class="contact-icon" viewBox="0 0 24 24" aria-hidden="true">
        <path d="M6.6 10.8a15.1 15.1 0 0 0 6.6 6.6l2.2-2.2c.3-.3.7-.4 1-.2 1.1.4 2.3.6 3.6.6.6 0 1 .4 1 1V20c0 .6-.4 1-1 1C10.6 21 3 13.4 3 4c0-.6.4-1 1-1h3.5c.6 0 1 .4 1 1 0 1.3.2 2.5.6 3.6.1.3 0 .7-.2 1z"/>
      </svg>
      <span>Phone Number: <span class="contact-value">0417 538 924</span></span>
    </div>
    <div class="contact-line">
      <svg class="contact-icon mail" viewBox="0 0 46 30" aria-hidden="true">
        <path d="M0 0h46v30H0z M3 3v1l20 14L43 4V3z M3 8v19h40V8L23 22z" fill-rule="evenodd"/>
      </svg>
      <span>Email: <span class="contact-value">dario@bravenvoltworks.com</span></span>
    </div>
  </address>
</main>
</body>
</html>
```